QTV Advisory needs business card

Having just developed a logo, I now want to use that logo in the development of a business card. The card should contain the logo, my name, title, phone, email, website and physical address. I would like to use one side of the card for details and the other side for logo and messaging. Use your creativity to place the information effectively. I want the logo to appear in a strong blue, which may be matched on the back side of the card, where the logo might be reversed out in white. I want the text to be in either dark blue or black (not light blue or gray).
I am consultant, primarily helping small and mid-size companies refine their strategy, reorganize their staff and propel forward in their industry. I also teach at universities and coach on a one-on-one basis. The final design should reflect expertise, guidance, judgement, perspective, experience.
The font used in the logo is ACaslonPro.

Target Market(s)

small to mid-size companies in the US seeking business guidance

Industry/Entity Type

Business

Font styles to use
Other font styles liked:
• ACaslonPro

Colors
0455a3
0255a3
3277b5

Requirements
Must have
• Card must convey my name and information clearly. Do not make it too small - many of my customers are 50+ years old. Please use all three of my titles: consultant / coach / instructor.
Should not have
• Please do not use icons to represent the phone, email, web. Do not use p / e / w either to indicate those details.

I have decided that a swatch of color, especially a "blue wave," does not work for me. I would rather have a simpler, more reserved look rather than a very contemporary, high color card.

Please do not deconstruct the logo or put it in a different font or italics.

```html
<!DOCTYPE html>
<html lang="en">
<head>
<meta charset="utf-8">
<title>QTV Advisory Business Card</title>
<link rel="stylesheet" href="https://fonts.googleapis.com/css2?family=Libre+Caslon+Text:wght@400;700&display=swap">
<style>
  :root {
    --page: #e9e6e1;
    --blue-deep: #0455a3;
    --blue-mid: #1a72c4;
    --blue-light: #5d9dd2;
    --paper: #ffffff;
    --ink-dark: #123a66;
    --stripe: #f1f4f8;
  }
  html, body {
    margin: 0;
    width: 1200px;
    height: 900px;
    overflow: hidden;
    background: var(--page);
    font-family: "Libre Caslon Text", Georgia, serif;
  }
  .card {
    position: absolute;
    left: 250px;
    width: 700px;
    height: 400px;
    overflow: hidden;
    box-shadow: 0 6px 18px rgba(0,0,0,0.18);
  }
  .card-details { top: 34px; background: var(--blue-mid); }
  .card-brand { top: 466px; background: var(--paper); }
  .card svg.shapes { position: absolute; inset: 0; }

  .holder {
    position: absolute;
    left: 34px;
    bottom: 34px;
    color: var(--paper);
  }
  .holder-name {
    margin: 0;
    font-size: 34px;
    font-weight: 400;
    line-height: 1.1;
  }
  .holder-credential {
    margin: 2px 0 0;
    font-size: 26px;
    line-height: 1.15;
  }
  .holder-titles {
    margin: 18px 0 0;
    font-size: 15px;
    letter-spacing: 0.3px;
  }

  .contact-list {
    position: absolute;
    top: 22px;
    left: 318px;
    margin: 0;
    padding: 0;
    list-style: none;
    color: var(--ink-dark);
    font-size: 19px;
  }
  .contact-list li {
    height: 34px;
    line-height: 34px;
    margin-bottom: 4px;
    padding-left: 26px;
  }

  .brand-name {
    position: absolute;
    left: 300px;
    top: 172px;
    display: flex;
    align-items: center;
    gap: 14px;
    color: var(--blue-deep);
    font-size: 38px;
    font-weight: 400;
    margin: 0;
    white-space: nowrap;
  }
  .brand-mark {
    width: 22px;
    height: 22px;
    background: var(--blue-deep);
  }
</style>
</head>
<body>

<section class="card card-details" aria-label="Card back with contact details">
  <svg class="shapes" width="700" height="400" viewBox="0 0 700 400" aria-hidden="true">
    <rect width="700" height="400" fill="var(--blue-mid)"/>
    <polygon points="0,0 90,0 370,400 0,400" fill="var(--blue-deep)" opacity="0.55"/>
    <polygon points="90,0 240,0 520,400 370,400" fill="var(--blue-light)"/>
    <line x1="90" y1="0" x2="370" y2="400" stroke="#dfe9f4" stroke-width="2"/>
    <g fill="var(--stripe)">
      <rect x="318" y="22" width="360" height="34"/>
      <rect x="318" y="60" width="360" height="34"/>
      <rect x="318" y="98" width="360" height="34"/>
      <rect x="318" y="136" width="360" height="34"/>
      <rect x="318" y="174" width="360" height="34"/>
    </g>
  </svg>

  <div class="holder">
    <h1 class="holder-name">R. Dalton</h1>
    <p class="holder-credential">Whitfield,<br>MBA</p>
    <p class="holder-titles">Consultant / Coach / Instructor</p>
  </div>

  <ul class="contact-list">
    <li>2150 Larkspur Lane</li>
    <li>Tampa, FL 33602</li>
    <li>(555) 014-2290</li>
    <li>www.qtv-advisory.com</li>
    <li>Dalton@qtv-advisory.com</li>
  </ul>
</section>

<section class="card card-brand" aria-label="Card front with company name">
  <svg class="shapes" width="700" height="400" viewBox="0 0 700 400" aria-hidden="true">
    <polygon points="0,0 170,0 262,400 0,400" fill="var(--blue-mid)"/>
  </svg>
  <p class="brand-name"><span class="brand-mark"></span>QTV Advisory</p>
</section>

</body>
</html>
```